Thank You Card

I'm looking for a thank you card design using our logo and other graphics. We are an essential business and our employees (Electricians) have done an incredible job staying healthy and safe during the COVID-19 pandemic, I want to send each a thank you card.

```html
<!DOCTYPE html>
<html lang="en">
<head>
<meta charset="utf-8">
<title>Thank You Card</title>
<link rel="stylesheet" href="https://fonts.googleapis.com/css2?family=Fira+Sans:wght@800&family=Fira+Sans+Condensed:wght@700&display=swap">
<style>
  :root {
    --backdrop: #e4e4e4;
    --navy: #0d2a8c;
    --navy-deep: #081f78;
    --navy-light: #16369e;
    --coral: #ef3a5d;
    --heart-red: #e0122e;
    --white: #ffffff;
  }
  html, body {
    margin: 0;
    padding: 0;
    width: 1200px;
    height: 900px;
    overflow: hidden;
    background: var(--backdrop);
  }
  .thank-you-card {
    position: absolute;
    left: 40px;
    top: 56px;
    width: 1120px;
    height: 788px;
    display: block;
  }
  .brand-name {
    font-family: "Fira Sans", sans-serif;
    font-weight: 800;
    fill: var(--white);
  }
  .banner-text {
    font-family: "Fira Sans Condensed", sans-serif;
    font-weight: 700;
    fill: var(--white);
    letter-spacing: 0.5px;
  }
  .headline {
    font-family: "Fira Sans", sans-serif;
    font-weight: 800;
    fill: var(--white);
  }
</style>
</head>
<body>
<svg class="thank-you-card" viewBox="0 0 930 655" xmlns="http://www.w3.org/2000/svg" role="group" aria-label="Thank you card for employees">
  <defs>
    <radialGradient id="card-glow" cx="50%" cy="50%" r="70%">
      <stop offset="0" stop-color="var(--navy-light)"/>
      <stop offset="0.6" stop-color="var(--navy)"/>
      <stop offset="1" stop-color="var(--navy-deep)"/>
    </radialGradient>
    <radialGradient id="dot-fade-tl" cx="0" cy="0" r="1">
      <stop offset="0" stop-color="var(--coral)" stop-opacity="0.85"/>
      <stop offset="1" stop-color="var(--coral)" stop-opacity="0"/>
    </radialGradient>
    <radialGradient id="dot-fade-tr" cx="1" cy="0" r="1">
      <stop offset="0" stop-color="var(--coral)" stop-opacity="0.85"/>
      <stop offset="1" stop-color="var(--coral)" stop-opacity="0"/>
    </radialGradient>
    <radialGradient id="dot-fade-bl" cx="0" cy="1" r="1">
      <stop offset="0" stop-color="var(--coral)" stop-opacity="0.85"/>
      <stop offset="1" stop-color="var(--coral)" stop-opacity="0"/>
    </radialGradient>
    <radialGradient id="dot-fade-br" cx="1" cy="1" r="1">
      <stop offset="0" stop-color="var(--coral)" stop-opacity="0.85"/>
      <stop offset="1" stop-color="var(--coral)" stop-opacity="0"/>
    </radialGradient>
    <path id="top-arc" d="M 305 222 Q 465 100 628 222"/>
    <path id="bottom-arc" d="M 305 548 Q 470 650 668 530"/>
  </defs>

  <rect class="card-ground" width="930" height="655" fill="url(#card-glow)" role="img" aria-label="Navy background with soft radiating light rays"/>

  <g class="corner-halftones" role="img" aria-label="Coral halftone dot patterns fading in from each corner">
    <rect x="0" y="0" width="200" height="240" fill="url(#dot-fade-tl)"/>
    <rect x="730" y="0" width="200" height="240" fill="url(#dot-fade-tr)"/>
    <rect x="0" y="400" width="210" height="255" fill="url(#dot-fade-bl)"/>
    <rect x="720" y="400" width="210" height="255" fill="url(#dot-fade-br)"/>
  </g>

  <g class="brand-lockup">
    <text class="brand-name" x="480" y="62" text-anchor="middle" font-size="40">BRIGHTLINE</text>
    <text class="brand-name" x="480" y="98" text-anchor="middle" font-size="24">ELECTRIC SERVICES</text>
  </g>

  <g class="top-banner">
    <path d="M 290 228 Q 465 92 640 228" fill="none" stroke="var(--coral)" stroke-width="34"/>
    <text class="banner-text" font-size="27" text-anchor="middle" dy="10">
      <textPath href="#top-arc" startOffset="50%">STAY SAFE • STAY HEALTHY</textPath>
    </text>
  </g>

  <g class="bottom-banner">
    <path d="M 262 518 Q 470 680 698 512" fill="none" stroke="var(--coral)" stroke-width="40"/>
    <text class="banner-text" font-size="34" text-anchor="middle" dy="6">
      <textPath href="#bottom-arc" startOffset="50%">FOR INCREDIBLE JOB</textPath>
    </text>
  </g>

  <g class="headline-group" transform="rotate(-6 480 440)">
    <text class="headline" x="478" y="392" text-anchor="middle" font-size="188" textLength="480" lengthAdjust="spacingAndGlyphs">Thank</text>
    <text class="headline" x="498" y="532" text-anchor="middle" font-size="182" textLength="320" lengthAdjust="spacingAndGlyphs">You!</text>
  </g>

  <g class="heart heart-left" transform="translate(215 358)">
    <path d="M 0 28 L -26 2 A 14 14 0 0 1 0 -16 Z" fill="var(--heart-red)"/>
    <path d="M 0 28 L 26 2 A 14 14 0 0 0 0 -16 Z" fill="var(--coral)"/>
  </g>
  <g class="heart heart-right" transform="translate(712 372)">
    <path d="M 0 28 L -26 2 A 14 14 0 0 1 0 -16 Z" fill="var(--heart-red)"/>
    <path d="M 0 28 L 26 2 A 14 14 0 0 0 0 -16 Z" fill="var(--coral)"/>
  </g>
</svg>
</body>
</html>
```